Designs for a Barrister's chambers

Design stationery (including business card and letterhead) for a barrister's chambers -- similar to a law firm, using the enclosed logo. The current designs are not fit for purpose.

```html
<!DOCTYPE html>
<html lang="en">
<head>
<meta charset="utf-8">
<title>Vellmont Chambers — Letterhead</title>
<link rel="stylesheet" href="https://fonts.googleapis.com/css2?family=Open+Sans:wght@400;600&family=Outfit:wght@500&display=swap">
<style>
  :root {
    --navy: #131e33;
    --teal: #0a93b5;
    --paper: #ffffff;
    --backdrop: #adadad;
    --ink-light: #ffffff;
  }
  * { margin: 0; padding: 0; box-sizing: border-box; }
  html, body {
    width: 1200px;
    height: 1200px;
    overflow: hidden;
    background: var(--backdrop);
  }
  .letterhead {
    position: absolute;
    left: 203px;
    top: 40px;
    width: 793px;
    height: 1120px;
    background: var(--paper);
  }
  .letterhead__header {
    position: absolute;
    left: 0;
    top: 0;
    width: 793px;
    height: 157px;
    display: block;
  }
  .brand {
    position: absolute;
    left: 31px;
    top: 45px;
    display: flex;
    align-items: center;
    gap: 14px;
  }
  .brand__square {
    width: 64px;
    height: 64px;
    background: var(--teal);
  }
  .brand__name {
    font-family: "Outfit", sans-serif;
    font-weight: 500;
    font-size: 33px;
    line-height: 36px;
    color: var(--ink-light);
    letter-spacing: -0.3px;
  }
  .registration {
    position: absolute;
    right: 54px;
    top: 38px;
    font-family: "Open Sans", sans-serif;
    font-weight: 600;
    font-size: 13px;
    color: var(--ink-light);
    word-spacing: 1px;
  }
  .registration span + span { margin-left: 14px; }
  .company-title {
    position: absolute;
    right: 53px;
    top: 92px;
    font-family: "Open Sans", sans-serif;
    font-weight: 600;
    font-size: 22px;
    letter-spacing: 1px;
    color: var(--ink-light);
  }
  .letterhead__footer {
    position: absolute;
    left: 0;
    top: 1021px;
    width: 793px;
    height: 70px;
    background: var(--navy);
    color: var(--ink-light);
    font-family: "Open Sans", sans-serif;
    font-size: 12px;
    line-height: 15px;
  }
  .contact {
    position: absolute;
    top: 17px;
    display: flex;
    align-items: center;
    gap: 14px;
  }
  .contact--phone { left: 62px; }
  .contact--web { left: 243px; }
  .contact--address { left: 529px; }
  .contact__icon { flex: none; display: block; }
</style>
</head>
<body>
  <main class="letterhead">
    <svg class="letterhead__header" viewBox="0 0 1012 200" preserveAspectRatio="none" aria-hidden="true">
      <path fill="var(--navy)" d="M0 0 H1012 V89 H462 Q448 89 440 100 L392 175 Q375 199 350 199 H0 Z"/>
      <path fill="var(--teal)" d="M462 89 H1012 V185 H392 L440 100 Q448 89 462 89 Z"/>
    </svg>

    <div class="brand">
      <div class="brand__square"></div>
      <div class="brand__name">Vellmont<br>Chambers</div>
    </div>

    <p class="registration"><span>VAT : 40817265</span><span>REG : 40817265</span></p>
    <h1 class="company-title">VELLMONT CHAMBERS LIMITED</h1>

    <footer class="letterhead__footer">
      <div class="contact contact--phone">
        <svg class="contact__icon" width="26" height="36" viewBox="0 0 26 36" aria-hidden="true">
          <rect x="1.5" y="1.5" width="23" height="33" rx="2.5" fill="none" stroke="#fff" stroke-width="1.6"/>
          <line x1="1.5" y1="6.5" x2="24.5" y2="6.5" stroke="#fff" stroke-width="1.2"/>
          <line x1="1.5" y1="29" x2="24.5" y2="29" stroke="#fff" stroke-width="1.2"/>
          <line x1="11" y1="32" x2="15" y2="32" stroke="#fff" stroke-width="1.2"/>
        </svg>
        <div>+0203 555 0100<br>+0203 555 0102</div>
      </div>
      <div class="contact contact--web">
        <svg class="contact__icon" width="32" height="24" viewBox="0 0 32 24" aria-hidden="true">
          <rect x="1" y="1" width="30" height="22" rx="2" fill="none" stroke="#fff" stroke-width="1.6"/>
          <path d="M1.5 2 L16 14 L30.5 2 M1.5 22 L12 11 M30.5 22 L20 11" fill="none" stroke="#fff" stroke-width="1.4"/>
        </svg>
        <div>www.vellmontchambers.com<br>clerks@vellmontchambers.com</div>
      </div>
      <div class="contact contact--address">
        <svg class="contact__icon" width="26" height="36" viewBox="0 0 26 36" aria-hidden="true">
          <path d="M13 34 C13 34 2 21 2 12.5 A11 11 0 0 1 24 12.5 C24 21 13 34 13 34 Z" fill="none" stroke="#fff" stroke-width="1.6"/>
          <circle cx="13" cy="12.5" r="4.5" fill="none" stroke="#fff" stroke-width="1.6"/>
        </svg>
        <div>42 Quill Lane, London<br>EC4X 9ZZ</div>
      </div>
    </footer>
  </main>
</body>
</html>
```